First Aid Training business needs business card design

We would like a double sided business card designed for a first aid training business - Brindlewood First Aid. We provide first aid training and , WHS (work, health and safety) training.

The attached word document contains the key information we would like on each side of the business card.

Final design needs to be delivered in print ready format, along with the original file.

```html
<!DOCTYPE html>
<html lang="en">
<head>
<meta charset="utf-8">
<title>Brindlewood First Aid – Business Card</title>
<link rel="stylesheet" href="https://fonts.googleapis.com/css2?family=Josefin+Sans:wght@300;400;700&family=Montserrat:wght@700&display=swap">
<style>
  :root {
    --bg: #c9c9c9;
    --white: #ffffff;
    --red: #ff0f17;
    --grey: #6b7b7a;
    --black: #0a0a0a;
    --ink: #111111;
  }
  * { box-sizing: border-box; margin: 0; padding: 0; }
  html, body { width: 1200px; height: 846px; overflow: hidden; background: var(--bg); }
  .canvas { position: relative; width: 1200px; height: 846px; }

  .card { position: absolute; left: 344px; width: 508px; height: 290px; overflow: hidden; }
  .card--front { top: 114px; background: var(--white); }
  .card--back { top: 444px; background: var(--red); }

  /* brand block */
  .brand-dot { position: absolute; border-radius: 50%; }
  .card--front .brand-dot { left: 90px; top: 54px; width: 90px; height: 90px; background: var(--red); }
  .card--back .brand-dot { left: 98px; top: 62px; width: 92px; height: 92px; background: var(--white); }

  .brand-name { position: absolute; font-family: "Montserrat", sans-serif; font-weight: 700; line-height: 1; white-space: nowrap; }
  .brand-name span { display: block; }
  .card--front .brand-name { left: 40px; top: 166px; width: 184px; text-align: center; color: var(--ink); }
  .card--front .brand-main { font-size: 21px; letter-spacing: -0.2px; }
  .card--front .brand-sub { font-size: 15px; margin-top: 9px; }
  .card--back .brand-name { left: 218px; top: 84px; color: var(--white); }
  .card--back .brand-main { font-size: 30px; letter-spacing: -0.3px; }
  .card--back .brand-sub { font-size: 17.5px; margin-top: 7px; }

  .divider { position: absolute; left: 234px; top: 165px; width: 1px; height: 54px; background: var(--grey); }

  /* contact block */
  .person { position: absolute; left: 254px; top: 106px; font-family: "Josefin Sans", sans-serif; font-weight: 700; font-size: 24px; letter-spacing: 0.5px; color: var(--ink); white-space: nowrap; }
  .person .surname { color: var(--red); margin-left: 4px; }

  .contacts { position: absolute; left: 252px; top: 160px; list-style: none; font-family: "Josefin Sans", sans-serif; font-weight: 300; font-size: 14.5px; color: var(--ink); letter-spacing: 0.3px; white-space: nowrap; }
  .contacts li { display: flex; align-items: center; height: 20.5px; }
  .contacts svg { width: 16px; height: 16px; margin-right: 7px; flex: none; }

  .stripe { position: absolute; left: 0; width: 100%; }
  .stripe--grey { top: 254px; height: 5px; background: var(--grey); }
  .stripe--black { top: 259px; height: 7px; background: var(--black); }
  .stripe--red { top: 266px; height: 24px; background: var(--red); }

  /* back side text */
  .offer { position: absolute; left: 0; width: 100%; text-align: center; color: var(--white); font-family: "Josefin Sans", sans-serif; white-space: nowrap; }
  .offer-title { top: 195px; font-weight: 700; font-size: 22px; letter-spacing: 0.6px; }
  .offer-points { top: 226px; font-weight: 300; font-size: 15px; letter-spacing: 0.4px; }
  .offer-services { top: 248px; font-weight: 300; font-size: 15px; letter-spacing: 0.4px; }
</style>
</head>
<body>
<main class="canvas">

  <section class="card card--front" aria-label="Business card front">
    <div class="brand-dot" aria-hidden="true"></div>
    <div class="brand-name">
      <span class="brand-main">BRINDLEWOOD</span>
      <span class="brand-sub">FIRST AID TRAINING</span>
    </div>
    <div class="divider" aria-hidden="true"></div>

    <h1 class="person">DANIEL <span class="surname">HARTLEY</span></h1>

    <ul class="contacts">
      <li>
        <svg viewBox="0 0 16 16" aria-hidden="true"><path fill="var(--red)" d="M4.2 1.2l2 2.6-1.3 1.4c.7 2.4 2.3 4.5 4.5 5.9l1.4-1.2 2.6 2-1.6 2.4C7 13.6 2.6 8.4 1.8 3z"/></svg>
        0491 570 226
      </li>
      <li>
        <svg viewBox="0 0 16 16" aria-hidden="true"><rect x="1" y="3" width="14" height="10" fill="var(--red)"/><path d="M1.5 3.5L8 9l6.5-5.5M1.5 12.5l5-4.5M14.5 12.5l-5-4.5" stroke="var(--white)" stroke-width="1" fill="none"/></svg>
        help@brindlewoodfirstaid.com.au
      </li>
      <li>
        <svg viewBox="0 0 16 16" aria-hidden="true"><g fill="none" stroke="var(--red)" stroke-width="1.2"><circle cx="8" cy="8" r="6.6"/><ellipse cx="8" cy="8" rx="3" ry="6.6"/><path d="M1.4 8h13.2M2.4 4.6h11.2M2.4 11.4h11.2M8 1.4v13.2"/></g></svg>
        www.brindlewoodfirstaid.com.au
      </li>
    </ul>

    <div class="stripe stripe--grey" aria-hidden="true"></div>
    <div class="stripe stripe--black" aria-hidden="true"></div>
    <div class="stripe stripe--red" aria-hidden="true"></div>
  </section>

  <section class="card card--back" aria-label="Business card back">
    <div class="brand-dot" aria-hidden="true"></div>
    <div class="brand-name">
      <span class="brand-main">BRINDLEWOOD</span>
      <span class="brand-sub">FIRST AID TRAINING</span>
    </div>

    <p class="offer offer-title">Onsite Training - We can come to you</p>
    <p class="offer offer-points">• Time efficient • Cost effective • Minimise downtime for your team</p>
    <p class="offer offer-services">First Aid Training &amp; WHS Training</p>
  </section>

</main>
</body>
</html>
```